Flyer for American Indian Elders on Dementia Warning Signs

We need a flyer designed for older adults who are American Indian or Alaska Native (in the U.S.).

Ideally, the flyer should complement the colors of our logos. The project logo and our organization logo are attached to the brief.

When people see the flyer we want them to feel that it represents their culture, is warm, and professional but relatable to older adults and people who have limited incomes.

I have attached an earlier draft of the document we designed ourselves BUT we want different and better.

It is for older adults who have trouble reading so:
1. you must use a font that is 11.5 points or larger
2. Do not put text over complex pictures or use shading with words
3. You can use a serif font for the heading, but should use san serif for the body text
4. There should be good contrast between the font color and background

Please do not use any images that include a head dress or pictures of American Indian people or things that are very traditional or "token" imagery.

We need to save a small space under the call out box/ somewhere on the flyer for other people to add their logo once they download.

Let us know if you have questions or need additional information.

Target Market(s)

Older American Indian people

Font styles to use
Serif
Sans Serif

Requirements
Must have
• Easy to read for older adults
Should not have
• indian headdress

```html
<!DOCTYPE html>
<html lang="en">
<head>
<meta charset="utf-8">
<title>10 Signs of Thinking or Memory Changes that Might be Dementia</title>
<link rel="stylesheet" href="https://fonts.googleapis.com/css2?family=Lato:wght@400;700&family=Merriweather:wght@700;900&family=Oswald:wght@500;700&display=swap">
<style>
  :root {
    --clay: #b05c52;
    --clay-dark: #7d3a33;
    --teal: #52a9b2;
    --teal-text: #3f97a1;
    --ink: #2a2a2a;
    --paper: #ffffff;
  }
  * { margin: 0; padding: 0; box-sizing: border-box; }
  html, body { width: 990px; height: 1200px; overflow: hidden; background: var(--paper); }
  body { font-family: "Lato", sans-serif; color: var(--ink); }
  .flyer { position: relative; width: 990px; height: 1200px; background: var(--paper); overflow: hidden; }

  .header-shape { position: absolute; left: 0; top: 0; width: 990px; height: 322px; }

  .big-ten {
    position: absolute; left: 52px; top: 40px;
    font-family: "Oswald", sans-serif; font-weight: 700; font-size: 165px; line-height: 1;
    color: var(--paper); letter-spacing: -8px;
    text-shadow: 5px 5px 0 var(--clay-dark);
  }
  .signs-of {
    position: absolute; left: 184px; top: 64px; height: 36px; width: 112px;
    background: var(--paper); clip-path: polygon(0 0, 100% 0, 92% 100%, 0 100%);
    font-family: "Oswald", sans-serif; font-weight: 500; font-size: 29px; line-height: 36px;
    color: var(--clay); padding-left: 6px; letter-spacing: -0.5px;
  }
  .title {
    position: absolute; left: 200px; top: 60px;
    font-family: "Merriweather", serif; font-weight: 900; font-size: 31px; line-height: 40px;
    color: var(--paper);
  }
  .title .first-line { padding-left: 102px; }

  .org-mark { position: absolute; left: 548px; top: 62px; display: flex; align-items: center; gap: 12px; }
  .org-mark .dot { width: 44px; height: 44px; border-radius: 50%; background: var(--teal); }
  .org-mark .name {
    font-family: "Lato", sans-serif; font-weight: 700; font-size: 21px; line-height: 24px;
    color: var(--teal-text); text-transform: uppercase; border-left: 2px solid var(--teal); padding-left: 12px;
  }

  .intro { position: absolute; left: 60px; top: 204px; width: 880px; }
  .intro p {
    color: var(--paper); font-size: 16px; line-height: 21px;
    border-left: 3px solid var(--paper); padding-left: 13px; margin-bottom: 13px;
  }

  .sign { position: absolute; left: 57px; width: 520px; }
  .sign h2 { font-size: 18px; line-height: 23px; font-weight: 700; color: var(--teal-text); padding-left: 26px; position: relative; }
  .sign h2 .lead { font-weight: 400; color: var(--ink); }
  .num {
    position: absolute; left: 0; top: 3px; width: 19px; height: 19px; border-radius: 50%;
    background: var(--teal); color: var(--paper); font-size: 9.5px; font-weight: 700;
    line-height: 19px; text-align: center;
  }
  .sign ul { list-style: none; padding-left: 26px; margin-top: 2px; }
  .sign li { font-size: 16px; line-height: 22.5px; padding-left: 22px; position: relative; }
  .sign li svg { position: absolute; left: 0; top: 5px; width: 13px; height: 13px; }
  .sign .wide { width: 560px; }

  .callout { position: absolute; left: 596px; top: 321px; width: 333px; height: 612px; }
  .callout-shape { position: absolute; left: 0; top: 0; width: 333px; height: 612px; }
  .facts { position: absolute; left: 0; top: 18px; width: 333px; text-align: center; color: var(--paper); }
  .facts p { font-size: 16px; line-height: 20.5px; font-weight: 700; padding: 0 30px; }
  .facts hr { border: 0; border-top: 1px solid var(--paper); width: 256px; margin: 13px auto; }

  .learn { position: absolute; left: 583px; top: 720px; width: 355px; height: 142px; background: var(--clay); text-align: center; color: var(--paper); padding-top: 14px; }
  .learn p { font-size: 14px; line-height: 18.5px; padding: 0 30px; }
  .learn .url { font-size: 16px; font-weight: 700; line-height: 21px; display: block; padding: 7px 0; }
  .learn hr { border: 0; border-top: 1px solid var(--paper); width: 234px; margin: 0 auto; }

  .partner { position: absolute; left: 596px; top: 948px; display: flex; align-items: center; gap: 14px; }
  .partner .dot { width: 84px; height: 84px; border-radius: 50%; background: linear-gradient(180deg, var(--teal), var(--clay)); }
  .partner .name { font-size: 22px; line-height: 24px; font-weight: 700; color: var(--teal-text); text-transform: uppercase; }

  .sign.tenth { left: 748px; left: 748px; }
  .sign.tenth { left: 748px; }
  .footer-bar { position: absolute; left: 596px; top: 1191px; width: 333px; height: 9px; background: var(--clay); }
</style>
</head>
<body>
<svg width="0" height="0" style="position:absolute">
  <defs>
    <symbol id="tick" viewBox="0 0 14 14">
      <circle cx="7" cy="7" r="6" fill="none" stroke="#b05c52" stroke-width="1.2"/>
      <path d="M4.2 7.2 L6.2 9.1 L9.9 5" fill="none" stroke="#b05c52" stroke-width="1.3" stroke-linecap="round" stroke-linejoin="round"/>
    </symbol>
  </defs>
</svg>

<main class="flyer">
  <svg class="header-shape" viewBox="0 0 990 322" aria-hidden="true">
    <rect x="0" y="0" width="990" height="322" fill="#b05c52"/>
    <path d="M470 0 H990 V153 H612 C598 153 590 147 582 135 L500 10 C494 3 485 0 470 0 Z" fill="#ffffff"/>
    <path d="M470 8 C484 8 490 12 497 22 L574 140 C582 151 592 157 606 157 L596 153 C588 150 584 146 578 136 L504 18 C497 9 488 6 476 6 Z" fill="#52a9b2"/>
    <path d="M470 0 C486 0 494 4 500 12 L584 138 C590 147 598 153 612 153 L598 160 C586 158 578 152 571 141 L492 18 C486 10 479 7 468 7 Z" fill="#52a9b2"/>
  </svg>

  <div class="big-ten">10</div>
  <div class="signs-of">SIGNS OF</div>
  <h1 class="title"><span class="first-line">Thinking or</span><br>Memory Changes that<br>Might be Dementia</h1>

  <div class="org-mark">
    <span class="dot"></span>
    <span class="name">Native Elders<br>Wellness Alliance</span>
  </div>

  <section class="intro">
    <p>As you get older, we may slow down a bit. This is a normal part of aging. Changes in memory or thinking that make it harder to get through the day, are not a normal part of aging. These may be early signs of dementia.</p>
    <p>Because American Indian and Alaska Native people have a high risk of dementia, it is important to know the warning signs. Do you have any of these 10 signs? If so, talk to your doctor.</p>
  </section>

  <section class="sign" style="top:356px">
    <h2><span class="num">01</span>Memory loss that affects your daily life. You may:</h2>
    <ul>
      <li><svg><use href="#tick"/></svg>Forget events or important dates</li>
      <li><svg><use href="#tick"/></svg>Repeat yourself</li>
      <li><svg><use href="#tick"/></svg>Rely more often on lists or sticky notes to remember things</li>
    </ul>
  </section>

  <section class="sign" style="top:459px">
    <h2><span class="num">02</span>Trouble planning or solving problems. <span class="lead">You may have a harder time:</span></h2>
    <ul>
      <li><svg><use href="#tick"/></svg>Paying bills</li>
      <li><svg><use href="#tick"/></svg>Cooking recipes you have used for years</li>
    </ul>
  </section>

  <section class="sign" style="top:562px">
    <h2><span class="num">03</span>Get confused about the time, date, or where you are.</h2>
  </section>

  <section class="sign" style="top:599px">
    <h2><span class="num">04</span>Daily tasks are getting harder, including:</h2>
    <ul>
      <li><svg><use href="#tick"/></svg>Driving</li>
      <li><svg><use href="#tick"/></svg>Making a grocery list or going shopping</li>
    </ul>
  </section>

  <section class="sign" style="top:682px">
    <h2><span class="num">05</span>Trouble with how your eyesight and thinking work together that gets worse. <span class="lead">This includes:</span></h2>
    <ul>
      <li><svg><use href="#tick"/></svg>Tripping, falls, or problems with your balance</li>
      <li><svg><use href="#tick"/></svg>Spilling or dropping things more</li>
    </ul>
  </section>

  <section class="sign" style="top:790px">
    <h2><span class="num">06</span>New trouble talking or writing.</h2>
    <ul style="margin-top:6px">
      <li><svg><use href="#tick"/></svg>You have a hard time finding the words you want to say. For example, you may say “that thing on your wrist that tells time” instead of “watch.”</li>
    </ul>
  </section>

  <section class="sign" style="top:894px">
    <h2><span class="num">07</span>Lose and cannot find things. <span class="lead">For example, you:</span></h2>
    <ul>
      <li><svg><use href="#tick"/></svg>Can’t find the coffee pot that you use every day</li>
      <li><svg><use href="#tick"/></svg>Might put your car keys in the freezer</li>
    </ul>
  </section>

  <section class="sign" style="top:975px">
    <h2><span class="num">08</span>Notice changes in mood or personality, <span class="lead">such as being:</span></h2>
    <ul>
      <li><svg><use href="#tick"/></svg>Easily mad or sad in everyday situations</li>
      <li><svg><use href="#tick"/></svg>More fearful (scared) or suspicious (not trusting)</li>
    </ul>
  </section>

  <section class="sign wide" style="top:1057px">
    <h2><span class="num">09</span>Act different and make poor choices. <span class="lead">This may make<br>you more likely to:</span></h2>
    <ul>
      <li><svg><use href="#tick"/></svg>Spend money you do not have or be a scam victim</li>
      <li><svg><use href="#tick"/></svg>Stop washing up regularly or pay less attention to how you look</li>
      <li><svg><use href="#tick"/></svg>Forget to take care of your pet</li>
    </ul>
  </section>

  <aside class="callout">
    <svg class="callout-shape" viewBox="0 0 333 612" aria-hidden="true">
      <path d="M0 0 H333 V612 L167 545 L0 612 Z" fill="#52a9b2"/>
    </svg>
    <div class="facts">
      <p>American Indian and Alaska Native people have a high risk of dementia.</p>
      <hr>
      <p>Big changes in memory or thinking that make it hard to get through the day are not a normal part of aging.</p>
      <hr>
      <p>People with one or more of these 10 signs should talk to their doctor to find the cause. It is not always dementia.</p>
      <hr>
      <p>Early dementia diagnosis gives you a chance to get care and plan your future.</p>
    </div>
  </aside>

  <div class="learn">
    <p>To learn more about the warning signs of dementia in American Indian and Alaska Native people, visit:</p>
    <span class="url">www.NativeMindCare.org</span>
    <hr>
    <span class="url">www.elderhealthinfo.org</span>
  </div>

  <div class="partner">
    <span class="dot"></span>
    <span class="name">Tribal Elders<br>Brain Health Center</span>
  </div>

  <section class="sign" style="top:1055px; left:596px; width:340px">
    <h2 style="padding-left:32px"><span class="num" style="left:6px">10</span>Pull away from friends and family because it is harder to keep up.</h2>
    <ul style="padding-left:32px; margin-top:6px">
      <li><svg><use href="#tick"/></svg>You may not want to do things you used to enjoy, like sporting events, church, music, or sex.</li>
    </ul>
  </section>

  <div class="footer-bar"></div>
</main>
</body>
</html>
```